Stonebrook 720 Real Estate Investment Company

We need a business card designed for a real estate investment company named Stonebrook 720. We want to use red#f04a50, orange #f37122 and yellow #fbee3e as the color scheme. The logo colors will need to be modified from the current blue palette. I've attach VitaPathway logo example that captures the color scheme we're going for for Stonebrook 720. Looking for clean Sans Serif fonts.
Contact Information for Business Card
Daniel Furlow
Managing Partner
48317 Whitfield Lane, Suite 510
Tampa, FL 33718
813-555-4870 Mobile
dfurlow@stonebrook720.example
www.stonebrook720.example
Requirements
Must have
- Looking for creative responses.
Nice to have
- Must hit color palette... orange, red, yellow

```html
<!DOCTYPE html>
<html lang="en">
<head>
<meta charset="utf-8">
<title>Stonebrook 720 – Business Card</title>
<link href="https://fonts.googleapis.com/css2?family=Lato:wght@400;700;900&display=swap" rel="stylesheet">
<style>
  :root {
    --backdrop: #2c2c2c;
    --card-white: #ffffff;
    --brand-red: #f04a50;
    --brand-orange: #f37122;
    --brand-yellow: #fbee3e;
    --ink: #231f20;
    --text: #222222;
  }
  * { margin: 0; padding: 0; box-sizing: border-box; }
  html, body {
    width: 1200px; height: 900px; overflow: hidden;
    background: var(--backdrop);
    font-family: "Lato", Arial, sans-serif;
  }
  .card {
    position: absolute;
    left: 261px;
    width: 656px;
    height: 358px;
    border-radius: 24px;
    overflow: hidden;
  }
  .card-front { top: 69px; background: var(--card-white); }
  .card-back { top: 472px; background: var(--brand-red); }

  .brand {
    position: absolute;
    display: flex;
    align-items: center;
    gap: 8px;
    font-weight: 900;
    letter-spacing: -0.5px;
  }
  .brand-mark { border-radius: 50%; flex: none; }
  .card-front .brand { left: 30px; top: 24px; font-size: 30px; color: var(--ink); }
  .card-front .brand-mark { width: 14px; height: 14px; background: var(--brand-orange); }
  .card-back .brand {
    left: 0; right: 0; top: 152px;
    justify-content: center;
    font-size: 42px; color: var(--card-white);
  }
  .card-back .brand-mark { width: 18px; height: 18px; background: var(--brand-yellow); }

  .person {
    position: absolute; right: 33px; top: 184px; text-align: right;
  }
  .person-name {
    font-size: 23px; font-weight: 700; letter-spacing: 1.2px;
    color: var(--brand-red); line-height: 28px;
  }
  .person-title { font-size: 17.5px; color: var(--text); line-height: 22px; }

  .divider {
    position: absolute; left: 30px; right: 33px; top: 246px;
    height: 1.5px; background: var(--brand-orange);
  }

  .contact-list {
    position: absolute; left: 30px; top: 268px; list-style: none;
  }
  .contact-list li {
    display: flex; align-items: center; gap: 9px;
    font-size: 17px; line-height: 21.5px; color: var(--text);
  }
  .contact-list svg { width: 11px; height: 11px; flex: none; }

  .address {
    position: absolute; right: 33px; top: 290px;
    text-align: right; font-size: 17px; line-height: 21.5px; color: var(--text);
    font-style: normal;
  }

  .accent-band { position: absolute; bottom: 0; height: 8px; }
  .accent-band-red { left: 0; width: 326px; background: var(--brand-red); }
  .accent-band-orange { left: 330px; right: 0; background: var(--brand-orange); }
</style>
</head>
<body>
  <section class="card card-front">
    <div class="brand"><span>Stonebrook720</span><span class="brand-mark"></span></div>

    <div class="person">
      <div class="person-name">DANIEL FURLOW</div>
      <div class="person-title">Managing Partner</div>
    </div>

    <div class="divider"></div>

    <ul class="contact-list">
      <li>
        <svg viewBox="0 0 12 12" aria-hidden="true"><path d="M2.5 1 L4.5 1 L5.2 3.6 L3.9 4.6 C4.6 6.2 5.8 7.4 7.4 8.1 L8.4 6.8 L11 7.5 L11 9.5 C11 10.4 10.3 11 9.5 11 C5 10.8 1.2 7 1 2.5 C1 1.7 1.6 1 2.5 1 Z" fill="var(--brand-red)"/></svg>
        813-555-4870
      </li>
      <li>
        <svg viewBox="0 0 12 12" aria-hidden="true"><rect x="1" y="2.5" width="10" height="7" rx="0.8" fill="none" stroke="var(--brand-red)" stroke-width="1.2"/><path d="M1.5 3 L6 6.5 L10.5 3" fill="none" stroke="var(--brand-red)" stroke-width="1.2"/></svg>
        dfurlow@stonebrook720.example
      </li>
      <li>
        <svg viewBox="0 0 12 12" aria-hidden="true"><g fill="none" stroke="var(--brand-red)" stroke-width="0.9"><circle cx="6" cy="6" r="5"/><ellipse cx="6" cy="6" rx="2.2" ry="5"/><path d="M1 6 H11 M1.8 3.5 H10.2 M1.8 8.5 H10.2"/></g></svg>
        www.stonebrook720.example
      </li>
    </ul>

    <address class="address">
      48317 Whitfield Lane,<br>
      Suite 510 Tampa, FL 33718
    </address>

    <div class="accent-band accent-band-red"></div>
    <div class="accent-band accent-band-orange"></div>
  </section>

  <section class="card card-back">
    <div class="brand"><span>Stonebrook720</span><span class="brand-mark"></span></div>
  </section>
</body>
</html>
```